Corvanta512 Business Card Redesign

I want to create a design for brand new business cards, I need something exceptional for clear plastic business card design. Please do not submit without it being on a clear design. Photos of the various logo versions attached.

```html
<!DOCTYPE html>
<html lang="en">
<head>
<meta charset="UTF-8">
<title>Corvanta512 Business Card</title>
<link rel="stylesheet" href="https://fonts.googleapis.com/css2?family=Manrope:wght@400;700;800&display=swap">
<style>
  :root {
    --backdrop: #eef1f5;
    --tint: rgba(52, 84, 128, 0.86);
    --tint-light: rgba(78, 110, 154, 0.80);
    --sheen: rgba(255, 255, 255, 0.10);
    --edge: rgba(255, 255, 255, 0.35);
    --gold: #f3d283;
    --gold-deep: #d9ac4e;
  }
  html, body {
    margin: 0;
    padding: 0;
    width: 1200px;
    height: 733px;
    overflow: hidden;
    background: var(--backdrop);
  }
  .card {
    position: relative;
    width: 1200px;
    height: 733px;
    box-sizing: border-box;
    border: 1px solid var(--edge);
    background:
      linear-gradient(125deg, var(--sheen) 0%, rgba(255,255,255,0) 38%, rgba(255,255,255,0) 70%, var(--sheen) 100%),
      linear-gradient(180deg, var(--tint-light) 0%, var(--tint) 100%);
    font-family: "Manrope", sans-serif;
    color: var(--gold);
  }
  .brand-mark {
    position: absolute;
    left: 50%;
    top: 72px;
    transform: translateX(-50%);
  }
  .brand-name {
    position: absolute;
    left: 0;
    right: 0;
    top: 328px;
    margin: 0;
    text-align: center;
    font-size: 74px;
    font-weight: 800;
    letter-spacing: 2px;
    color: var(--gold);
    line-height: 1;
  }
  .contact {
    position: absolute;
    left: 0;
    right: 0;
    margin: 0;
    text-align: center;
    line-height: 1;
    white-space: nowrap;
  }
  .person-name {
    top: 442px;
    font-size: 41px;
    font-weight: 700;
  }
  .person-email {
    top: 493px;
    font-size: 33px;
    font-weight: 400;
  }
  .phone {
    top: 553px;
    font-size: 33px;
    font-weight: 400;
  }
  .general-email {
    top: 601px;
    font-size: 33px;
    font-weight: 400;
  }
  .website {
    top: 645px;
    font-size: 35px;
    font-weight: 700;
  }
</style>
</head>
<body>
  <main class="card">
    <svg class="brand-mark" width="210" height="210" viewBox="0 0 210 210" aria-hidden="true">
      <circle cx="105" cy="105" r="100" fill="var(--gold-deep)"/>
    </svg>
    <h1 class="brand-name">Corvanta512</h1>
    <p class="contact person-name">Mireille Oduya-Halvorsen</p>
    <p class="contact person-email">mireille@corvanta-512.com</p>
    <p class="contact phone">(855)-CORVA-512</p>
    <p class="contact general-email">info@corvanta-512.com</p>
    <p class="contact website">www.corvanta-512.com</p>
  </main>
</body>
</html>
```